Brazilian publishing house needs a JAZZY poster

We're launching an international guerrilla marketing campaign for a biography about the greatest saxophonist ever, Dorian Mabry (also known as "Tusk"), so we need a poster that will be printed and pasted on walls and posts, on a regular sheet, size A4.

It must say "Tusk vive!" (which means "Tusk lives!" in Portuguese) and have the website, www.qvzt.example/tuskvive. All the rest is free. Jazzy, MINIMALIST, cool images with birds and saxophones (or birds becoming saxophones) are welcome. Also, please insert our logo (attached) somewhere, even if not big.

I like this campaign very much and you like something like that: https://pomeraltisca.strovelpress.example/

Hope to hear from you!

Marketing

• Easy to see and understand, like most guerrilla actions, without many colors

```html
<!DOCTYPE html>
<html lang="pt">
<head>
<meta charset="UTF-8">
<title>Tusk vive!</title>
<link rel="stylesheet" href="https://fonts.googleapis.com/css2?family=Josefin+Sans:wght@300;400&family=Libre+Baskerville:ital,wght@0,700;1,700&display=swap">
<style>
  :root {
    --paper: #ffffff;
    --signal-red: #f0141c;
    --ink: #1a1a1a;
    --sepia-dark: #4a2c18;
    --sepia-deep: #7a4a2a;
    --sepia-mid: #a9764f;
    --sepia-soft: #d2ab88;
    --sepia-light: #ead7c2;
    --brass: #b98a5e;
    --wash: #efe4cf;
  }
  * { margin: 0; padding: 0; box-sizing: border-box; }
  html, body {
    width: 839px;
    height: 1200px;
    overflow: hidden;
    background: var(--paper);
  }
  .poster {
    position: relative;
    width: 839px;
    height: 1200px;
    background: var(--paper);
    overflow: hidden;
  }
  .art {
    position: absolute;
  }
  .art-wash {
    left: 150px;
    top: 690px;
    width: 440px;
    height: 270px;
    border-radius: 46% 54% 40% 60% / 50% 40% 60% 50%;
    background: linear-gradient(160deg, var(--wash) 0%, #f5eee0 60%, rgba(255,255,255,0) 100%);
  }
  .art-player {
    left: 150px;
    top: 88px;
    width: 420px;
    height: 470px;
    border-radius: 44% 48% 20% 30% / 30% 34% 26% 40%;
    background: linear-gradient(155deg, var(--sepia-soft) 0%, var(--sepia-mid) 38%, var(--sepia-light) 78%, #f6ede2 100%);
  }
  .art-splash {
    left: 400px;
    top: 500px;
    width: 250px;
    height: 300px;
    border-radius: 50% 44% 56% 48% / 46% 52% 48% 54%;
    background: radial-gradient(ellipse at 50% 45%, var(--sepia-dark) 0%, var(--sepia-deep) 45%, var(--sepia-soft) 80%, var(--sepia-light) 100%);
  }
  .art-saxophone {
    left: 540px;
    top: 135px;
    width: 110px;
    height: 600px;
    border-radius: 40px 40px 60px 60px;
    background: linear-gradient(90deg, var(--sepia-deep) 0%, var(--brass) 45%, var(--sepia-light) 70%, var(--sepia-mid) 100%);
  }
  .headline {
    position: absolute;
    left: 0;
    top: 560px;
    width: 839px;
    height: 170px;
  }
  .headline text {
    font-family: "Josefin Sans", sans-serif;
    font-weight: 300;
    font-size: 186px;
    fill: var(--signal-red);
  }
  .campaign-url {
    position: absolute;
    left: 22px;
    top: 718px;
    font-family: "Libre Baskerville", serif;
    font-weight: 700;
    font-size: 18px;
    color: var(--ink);
    letter-spacing: -0.2px;
  }
  .campaign-url em {
    font-style: italic;
    font-size: 21px;
  }
  .publisher-mark {
    position: absolute;
    right: -4px;
    top: 1150px;
    font-family: "Josefin Sans", sans-serif;
    font-weight: 300;
    font-size: 24px;
    letter-spacing: 2px;
    color: var(--ink);
    text-transform: uppercase;
  }
</style>
</head>
<body>
  <main class="poster">
    <div class="art art-wash" role="img" aria-label="Pale beige ink wash strokes beneath the musician"></div>
    <div class="art art-player" role="img" aria-label="Sepia photograph of a saxophonist in a suit playing, with small flocks of birds flying beside him"></div>
    <div class="art art-splash" role="img" aria-label="Dark brown ink splatter bursting around the bell of the saxophone"></div>
    <div class="art art-saxophone" role="img" aria-label="Brass alto saxophone standing upright in front of the musician"></div>

    <svg class="headline" viewBox="0 0 839 170" aria-label="Tusk vive!">
      <text x="0" y="150" textLength="814" lengthAdjust="spacingAndGlyphs">TUSK VIVE!</text>
    </svg>

    <p class="campaign-url">www.qvzt.example/<em>tuskvive</em></p>

    <p class="publisher-mark">Valdermoss</p>
  </main>
</body>
</html>
```